Unique Business Card Design

Unique Business Card design for our orthotic and prosthetic company. Our logo is on our website, color is light blue. Unique shape (artificial leg shaped, vertical, etc..) preferred. Logo, business name, individual name and basic demographics needed.

Industry/Entity Type

Business

Contact Information for Business Card

Logo, Industry, Phone # Logo, "Prosthetic & Orthotic Services" Place to add individual name and contact info

Colors
cee9f5

Requirements
Must have
• The icon must be there, placement of "Prosthetic & Orthotic Services" can be moved
Nice to have
• Like the mix of light blue, and a little darker blue. One design included the icons from my website which was a nice touch

```html
<!DOCTYPE html>
<html lang="en">
<head>
<meta charset="utf-8">
<title>LimbWell Inc. Business Card</title>
<link href="https://fonts.googleapis.com/css2?family=Montserrat:wght@400;500;600;700&display=swap" rel="stylesheet">
<style>
  :root {
    --brand-blue: #1b63b4;
    --deep-blue: #154f94;
    --light-blue: #cee9f5;
    --ink: #1d1d1d;
    --paper: #ffffff;
    --backdrop: #2b2b2d;
  }
  * { box-sizing: border-box; margin: 0; padding: 0; }
  html, body { width: 1200px; height: 900px; overflow: hidden; }
  body {
    background: var(--backdrop);
    font-family: "Montserrat", Arial, sans-serif;
    position: relative;
  }
  .card {
    position: absolute;
    left: 290px;
    width: 620px;
    height: 354px;
    border-radius: 22px;
    overflow: hidden;
  }
  .card-front { top: 72px; background: var(--brand-blue); }
  .card-back { top: 474px; background: var(--paper); }
  .card-shapes { position: absolute; inset: 0; }

  /* front */
  .front-emblem {
    position: absolute; left: 240px; top: 20px;
    width: 140px; height: 140px; border-radius: 50%;
    background: var(--paper);
    display: flex; align-items: center; justify-content: center;
    color: var(--brand-blue); font-weight: 700; font-size: 18px; letter-spacing: 1px;
  }
  .service {
    position: absolute; width: 140px; text-align: center;
    color: var(--paper); font-size: 12.5px; font-weight: 600; letter-spacing: .5px;
  }
  .service-icon {
    display: block; width: 46px; height: 46px; margin: 0 auto 8px;
    border-radius: 50%;
    background: radial-gradient(circle at 40% 35%, #ffffff 0%, var(--light-blue) 45%, #7fb3de 100%);
    border: 2px solid rgba(255,255,255,.6);
  }
  .service-orthotics { left: 44px; top: 224px; }
  .service-prosthetics { left: 240px; top: 180px; }
  .service-vascular { left: 440px; top: 128px; }

  /* back */
  .brand-lockup { position: absolute; left: 34px; top: 32px; display: flex; align-items: center; gap: 16px; }
  .brand-dot { width: 78px; height: 78px; border-radius: 50%; background: var(--brand-blue); flex: none; }
  .brand-name { color: var(--brand-blue); font-size: 25px; font-weight: 700; letter-spacing: .5px; }
  .brand-tagline {
    border-top: 2px solid var(--brand-blue);
    margin-top: 4px; padding-top: 3px;
    color: var(--brand-blue); font-size: 12px; font-weight: 500;
  }
  .person { position: absolute; right: 34px; top: 38px; text-align: right; }
  .person-name { color: var(--brand-blue); font-size: 22px; font-weight: 700; }
  .person-title {
    color: var(--brand-blue); font-size: 13px; font-weight: 500;
  }
  .person-address {
    position: absolute; right: 34px; top: 118px; text-align: right;
    color: var(--ink); font-size: 14px; line-height: 1.4;
  }
  .contact-list { position: absolute; left: 34px; top: 220px; list-style: none; }
  .contact-list li {
    display: flex; align-items: center; gap: 12px;
    color: var(--ink); font-size: 15px; line-height: 22px; font-weight: 500;
  }
  .contact-list svg { width: 12px; height: 12px; fill: var(--brand-blue); flex: none; }
  .web-accent { color: var(--brand-blue); font-weight: 700; }
</style>
</head>
<body>

<section class="card card-front" aria-label="Card front">
  <svg class="card-shapes" viewBox="0 0 620 354" preserveAspectRatio="none" aria-hidden="true">
    <polygon points="0,306 250,306 300,290 620,290 620,354 0,354" fill="#ffffff"/>
  </svg>
  <div class="front-emblem">LIMBWELL</div>
  <div class="service service-orthotics"><span class="service-icon" role="img" aria-label="Orthotics icon"></span>ORTHOTICS</div>
  <div class="service service-prosthetics"><span class="service-icon" role="img" aria-label="Prosthetics icon"></span>PROSTHETICS</div>
  <div class="service service-vascular"><span class="service-icon" role="img" aria-label="Vascular icon"></span>VASCULAR</div>
</section>

<section class="card card-back" aria-label="Card back">
  <svg class="card-shapes" viewBox="0 0 620 354" preserveAspectRatio="none" aria-hidden="true">
    <line x1="34" y1="212" x2="586" y2="88" stroke="#1b63b4" stroke-width="2"/>
    <polygon points="500,172 620,172 620,354 452,354" fill="#1b63b4"/>
    <rect x="0" y="338" width="620" height="16" fill="#1b63b4"/>
  </svg>

  <div class="brand-lockup">
    <span class="brand-dot"></span>
    <div>
      <div class="brand-name">LIMBWELL INC.</div>
      <div class="brand-tagline">Prosthetic &amp; Orthotic Services</div>
    </div>
  </div>

  <div class="person">
    <div class="person-name">Mira Kalden</div>
    <div class="person-title">Orthotist/Prosthetist</div>
  </div>
  <div class="person-address">2210 Harbor Ave.<br>Brooklyn, NY 11234</div>

  <ul class="contact-list">
    <li><svg viewBox="0 0 12 12"><rect x="3" y="0" width="6" height="12" rx="1.5"/></svg><span>845-555-0142</span></li>
    <li><svg viewBox="0 0 12 12"><path d="M2 0l3 3-1.5 2a7 7 0 0 0 3.5 3.5L9 7l3 3-2 2C5 12 0 7 0 2z"/></svg><span>718.555.0170</span></li>
    <li><svg viewBox="0 0 12 12"><rect x="0" y="4" width="12" height="7" rx="1"/><rect x="3" y="0" width="6" height="4"/></svg><span>718.555.0193</span></li>
    <li><svg viewBox="0 0 12 12"><path d="M0 2h12v8H0z M0 2l6 5 6-5" stroke="#fff" stroke-width=".8"/></svg><span>mkalden@limbwellinc.com</span></li>
    <li><svg viewBox="0 0 12 12"><circle cx="6" cy="6" r="6"/></svg><span>www.<span class="web-accent">limbwellinc</span>.com</span></li>
  </ul>
</section>

</body>
</html>
```